Business Card and Letterhead for Juniper Anvil - (Have Logo)

Update 4: Removed company reg no from business card details as it looked a bit out of place. Updated services list.
UPDATE 3
Sorry, I got the address a little bit wrong, have updated it below. Sorry for any inconvenience caused.
UPDATE 2
Finally I have the details for the business cards and letterhead. Submissions already made do not have to be updated unless shortlisted, if all new submissions could include the details for me, Marcus, that would be very much appreciated and help with the final shortlist selection. I intend to share a shortlist of the three best entries with past and existing customers for their feedback and opinions. Thank you all again for your time.
Here are the details.
Marcus Telby
Web Developer
T: 01632 960 418
E: marcus@juniperanvil.example
www.juniperanvil.example
Professional Photography
Web Solutions & E-Commerce
Audio & HD Video Production
Marketing & Promotions
Identity and Branding
Juniper Anvil Ltd
Suite 20938, 3rd Floor
212-224 Orchard Lane
London, N7 9QX
Company Reg. No: 05829147
The order and the layout of the information are of course down to the design, but the company registration number should be smaller and less prominent. The formatting of the telephone and email address using a T: and an E: I am not sure about and again if it is Tel: or Email: or Icons is up to the design.
The Company No. on the letterhead should read (somewhere in small text along the bottom):
Juniper Anvil is a Ltd Company registered in England & Wales, Registration No. 05829147.
The second business card details are
Oliver Brackley
Photographer
T: 01632 960 418
E: oliver@juniperanvil.example
Everything else the same of course.
Thank you again for all the submissions so far.
END OF UPDATE 2
-
UPDATE 1: Please do not alter the logo nor the logo colours. (This was a previous pixel forum project and I am extremely happy with it. The icon can stand alone of course, but I have had to eliminate all entries that have made it black and white, or reversed the icon.) I would like to thank everyone that has participated so far and am very grateful for all your thought and time.
End of Update 1
-
Original Brief:
I have attached the logo vector file.
Following a superb logo from a previous Pixel Forum project I am now looking for a business card design and (although less important) a letterhead as well.
I must admit I tried to do it myself but could only come up with the usual amateur stuff that in comparison to the quality of the logo looked awful.
About Us
Juniper Anvil Ltd will be a new company due to start in January. It is really just me (a web developer) and my friend (a photographer). We will be aiming at the usual small to medium sized businesses in the local area, selling various digital services including photographic services to the public, web hosting and development, commercial photography, modelling services (not us!), full video and film production and possibly a bit of marketing as well. (Really it is anything we can do professionally all lumped together! We met running seperate businesses which have both since closed)
We will not be competing on price. We plan to be expensive but fair. Certainly not the cheapest.
What we are looking for
Business Card
I imagine a double sided business card, which will be used for more than one person. I imagine the front to be the same for everyone and the persons details to be on the back, although this is of course only my thoughts and I am of course completely open to any ideas.
The card could also have a services list or a bit about what we do on it. It might feature the website address, our business address (mail forwarding address) or our registered company number.
Or it might have none of that, we are completely open to any ideas and have no real fixed opinions. I just want it to be really nice :-)
Letterhead (secondary importance)
We will make our decision primarily on the business card, although a mathcing letterhead would be fantastic. Something standardish in format and simple, although again, all ideas are welcomed.
I hope that is enough information but if you have any questions I will answer them as fully and as quickly as possible.
Thank you once again and I really look forward to seeing your ideas and picking a winner.
Marcus T.
Small businesses AND the general public
Film Production

```html
<!DOCTYPE html>
<html lang="en">
<head>
<meta charset="utf-8">
<title>Juniper Anvil – Business Card</title>
<link rel="stylesheet" href="https://fonts.googleapis.com/css2?family=Source+Sans+3:wght@400;700&display=swap">
<style>
  :root {
    --backdrop: #eee8de;
    --card-dark: #3d3d3f;
    --card-light: #ffffff;
    --brand-red: #b5121b;
    --text-light: #f2f2f2;
    --text-grey: #555558;
    --logo-grey: #3a3a3c;
  }
  * { margin: 0; padding: 0; box-sizing: border-box; }
  html, body {
    width: 1200px;
    height: 900px;
    overflow: hidden;
    background: var(--backdrop);
    font-family: "Source Sans 3", "Myriad Pro", Arial, sans-serif;
  }
  .canvas { position: relative; width: 1200px; height: 900px; }

  .card {
    position: absolute;
    top: 306px;
    width: 504px;
    height: 288px;
    box-shadow: 0 2px 6px rgba(0,0,0,0.18);
  }

  /* Back: personal details */
  .card-back { left: 74px; background: var(--card-dark); color: var(--text-light); }
  .card-back .accent-band {
    position: absolute; left: 0; right: 0; bottom: 0; height: 20px;
    background: var(--brand-red);
  }
  .card-back .brand-square {
    position: absolute; left: 450px; top: 108px; width: 36px; height: 36px;
    background: var(--text-light);
  }
  .details {
    position: absolute; right: 80px; text-align: right;
    font-size: 13px; line-height: 16px;
  }
  .details.person { top: 108px; }
  .details .name {
    color: var(--brand-red); font-size: 16px; text-transform: uppercase;
    letter-spacing: 0.5px; line-height: 20px;
  }
  .details.company { top: 180px; }
  .contact-row { display: flex; justify-content: flex-end; }
  .contact-row .label { width: 34px; text-align: left; }
  .contact-row .value { width: 88px; text-align: left; }

  /* Front: identity */
  .card-front { left: 620px; background: var(--card-light); }
  .logo {
    position: absolute; left: 20px; top: 106px;
    display: flex; align-items: center; gap: 10px;
  }
  .logo .brand-square { width: 36px; height: 36px; background: var(--brand-red); }
  .logo .wordmark {
    font-weight: 700; font-size: 30px; color: var(--logo-grey);
    text-transform: uppercase; letter-spacing: 1px; line-height: 1;
  }
  .services {
    position: absolute; left: 60px; top: 248px;
    font-size: 15px; color: var(--text-grey);
  }
</style>
</head>
<body>
<div class="canvas">

  <section class="card card-back" aria-label="Business card back">
    <div class="details person">
      <p class="name">Marcus Telby</p>
      <p class="role">Web</p>
      <p class="email">marcus@juniperanvil.example</p>
    </div>
    <div class="brand-square"></div>
    <div class="details company">
      <p class="address">212-224 Orchard Lane, London, N7 9QX</p>
      <p class="contact-row"><span class="label">Ph</span><span class="value">+900.555.0141</span></p>
      <p class="contact-row"><span class="label">Cell</span><span class="value">+900.555.0142</span></p>
      <p class="contact-row"><span class="label">Fax</span><span class="value">+900.555.0143</span></p>
      <p class="web">www.juniperanvil.example</p>
    </div>
    <div class="accent-band"></div>
  </section>

  <section class="card card-front" aria-label="Business card front">
    <div class="logo">
      <span class="brand-square"></span>
      <span class="wordmark">Juniper Anvil</span>
    </div>
    <p class="services">photographic - web hosting - development</p>
  </section>

</div>
</body>
</html>
```